Updated Business Card for Optometry Practice

We're a growing optometry practice that is moving to a beautiful new office and we want to update our business card. We just updated our logo so the new card should reflect the new logo. Our practice continually invests in state of the art instruments to help us provide eye care that is thorough, comfortable, efficient and educational.

I've attached our current card and logo. You can reference this for the information I would like on the card. The tag line on the back is "We're changing the way you see."

Upon completion of this project we will need (amongst other formats) Photoshop files of the card so I can change employee names to print cards for each employee.

```html
<!DOCTYPE html>
<html lang="en">
<head>
<meta charset="utf-8">
<title>Brookfield Family Eyecare – Business Card</title>
<link href="https://fonts.googleapis.com/css2?family=Montserrat:wght@400;500;600;700&display=swap" rel="stylesheet">
<style>
  :root {
    --navy: #14284c;
    --gold: #d4ac2b;
    --white: #ffffff;
    --ink: #1d1d1f;
    --backdrop: #3a3a3c;
  }
  * { box-sizing: border-box; margin: 0; padding: 0; }
  html, body {
    width: 1200px; height: 1200px; overflow: hidden;
    background: var(--backdrop);
    font-family: "Montserrat", sans-serif;
  }
  .canvas {
    position: relative; width: 1200px; height: 1200px;
  }
  .card {
    position: absolute; left: 180px; width: 840px; height: 480px;
    border-radius: 36px; overflow: hidden;
  }
  .card--front { top: 80px; background: var(--white); }
  .card--back { top: 640px; background: var(--navy); }

  /* Front */
  .contact-block { position: absolute; left: 70px; top: 150px; }
  .person-name {
    color: var(--gold); font-weight: 600; font-size: 34px; letter-spacing: 0.5px;
  }
  .person-title {
    color: var(--ink); font-weight: 500; font-size: 17px; letter-spacing: 0.5px; margin-top: 2px;
  }
  .contact-list { list-style: none; margin-top: 22px; }
  .contact-item {
    display: flex; align-items: flex-start; gap: 12px;
    color: var(--ink); font-size: 17px; line-height: 1.5; margin-bottom: 4px;
  }
  .contact-item svg { flex: none; width: 20px; height: 20px; margin-top: 4px; }
  .practice-line { color: var(--gold); font-weight: 500; }

  .brand-front {
    position: absolute; right: 60px; top: 110px;
    display: flex; align-items: center; gap: 14px;
  }
  .brand-mark { width: 26px; height: 26px; border-radius: 50%; background: var(--gold); flex: none; }
  .brand-name {
    color: var(--navy); font-weight: 600; font-size: 30px; line-height: 1.15;
    letter-spacing: 1px; text-transform: uppercase;
  }

  .band { position: absolute; bottom: 0; }
  .band--gold { left: 0; width: 540px; height: 30px; background: var(--gold); }
  .band--navy { left: 554px; right: 0; height: 62px; background: var(--navy); }

  /* Back */
  .brand-back {
    position: absolute; left: 0; right: 0; top: 170px;
    display: flex; justify-content: center; align-items: center; gap: 20px;
  }
  .brand-back .brand-mark { width: 34px; height: 34px; }
  .brand-back .brand-name { color: var(--white); font-size: 44px; letter-spacing: 2px; }
  .tagline {
    position: absolute; left: 0; right: 0; bottom: 70px; text-align: center;
    color: var(--gold); font-weight: 600; font-size: 26px;
  }
</style>
</head>
<body>
<div class="canvas">

  <section class="card card--front">
    <div class="contact-block">
      <h1 class="person-name">DANIEL MERCER, OD</h1>
      <p class="person-title">OPTOMETRIST</p>
      <ul class="contact-list">
        <li class="contact-item">
          <svg viewBox="0 0 24 24"><path fill="#d4ac2b" d="M6.6 10.8a15.1 15.1 0 0 0 6.6 6.6l2.2-2.2a1 1 0 0 1 1-.25 11.4 11.4 0 0 0 3.6.57 1 1 0 0 1 1 1V20a1 1 0 0 1-1 1A17 17 0 0 1 3 4a1 1 0 0 1 1-1h3.5a1 1 0 0 1 1 1c0 1.25.2 2.45.57 3.57a1 1 0 0 1-.25 1z"/></svg>
          <span>(555) 208-3174</span>
        </li>
        <li class="contact-item">
          <svg viewBox="0 0 24 24"><rect x="2" y="5" width="20" height="14" rx="1.5" fill="#d4ac2b"/><path d="M3 6l9 7 9-7" fill="none" stroke="#fff" stroke-width="1.6"/></svg>
          <span>dan@brookfieldeyecare.com</span>
        </li>
        <li class="contact-item">
          <svg viewBox="0 0 24 24" fill="none" stroke="#d4ac2b" stroke-width="1.6"><circle cx="12" cy="12" r="9"/><ellipse cx="12" cy="12" rx="4" ry="9"/><path d="M3 12h18M4.5 7.5h15M4.5 16.5h15"/></svg>
          <span>www.brookfieldeyecare.com</span>
        </li>
        <li class="contact-item">
          <svg viewBox="0 0 24 24"><path fill="#d4ac2b" d="M12 2a7 7 0 0 0-7 7c0 5 7 13 7 13s7-8 7-13a7 7 0 0 0-7-7zm0 9.5A2.5 2.5 0 1 1 12 6.5a2.5 2.5 0 0 1 0 5z"/></svg>
          <span><span class="practice-line">Brookfield Family Eyecare</span><br>2870 Linden Ridge Dr #210<br>Maplewood, OH 45301</span>
        </li>
      </ul>
    </div>

    <div class="brand-front">
      <span class="brand-mark"></span>
      <span class="brand-name">Brookfield<br>Family Eyecare</span>
    </div>

    <div class="band band--gold"></div>
    <div class="band band--navy"></div>
  </section>

  <section class="card card--back">
    <div class="brand-back">
      <span class="brand-mark"></span>
      <span class="brand-name">Brookfield<br>Family Eyecare</span>
    </div>
    <p class="tagline">We're changing the way you see.</p>
  </section>

</div>
</body>
</html>
```